Pinebrook Commerce Estate Needs Website

We are looking to freshen up the look of our existing website using a new logo, company name and color scheme. Needs to be responsive and mobile friendly for all browsers and coded for both Android & IOS. SEO is also important. Want something visually grabbing that displays growth, quality and confidence.

WordPress or Joomla – must be desktop and mobile friendly with fast page load speed. Need the ability to edit ourselves.

Need interactive map where can mark as sold, pending, available with prices. Can keep existing map layout but it will need to be refreshed.
Will need instructions or to be shown how the map is edited to change from pending, sold, available, price etc.

Existing website:
https://example-lornavale.com/

READ ATTACHED WEBSITE BRIEF FOR COMPLETE DETAILS

I have included an old sales sheet you can take pictures from.

New logos attached.

Industry/Entity Type

Land Sale/Lease/Development

Coding

Coded - Design and coding required

Number of Pages Required

4 page

Requirements
Must have
• Interactive Map - Logo Colour BA000 (RED)

```html
<!DOCTYPE html>
<html lang="en">
<head>
<meta charset="utf-8">
<title>Pinebrook Commerce Estate</title>
<link href="https://fonts.googleapis.com/css2?family=Exo+2:wght@600;700;800&family=Roboto:wght@300;400;500;700&display=swap" rel="stylesheet">
<style>
:root{
  --red:#ba0000;
  --red-dark:#8e0000;
  --black:#000;
  --ink:#222;
  --page:#f8f8f8;
  --wave:#efefef;
  --maroon:#922a48;
  --gold:#f2cf6a;
  --field:#e7c8cf;
}
*{box-sizing:border-box;margin:0;padding:0}
html,body{width:1200px;height:3026px;overflow:hidden}
body{position:relative;background:var(--page);font-family:"Roboto",sans-serif;color:var(--ink)}
.abs{position:absolute}
.heading{font-family:"Exo 2",sans-serif;font-weight:800}

/* header */
.site-header{left:0;top:0;width:1200px;height:108px;background:#fff}
.brand{left:65px;top:22px;display:flex;align-items:center;gap:12px}
.brand-dot{width:62px;height:62px;border-radius:50%;background:var(--red)}
.brand-name{font-family:"Exo 2",sans-serif;font-weight:800;color:var(--red);font-size:24px;line-height:1.05;width:190px}
.nav{top:47px;left:455px;display:flex;gap:40px;font-size:14px;font-weight:500;color:#111}
.nav .active{color:var(--red)}
.btn{display:flex;align-items:center;justify-content:center;border-radius:22px;font-family:"Exo 2",sans-serif;font-weight:700}
.btn-red{background:var(--red);color:#fff}
.btn-outline-red{border:2px solid var(--red);color:var(--red);background:#fff}
.btn-outline-white{border:2px solid #fff;color:#fff}
.quick{left:980px;top:35px;width:155px;height:38px;font-size:16px}

/* hero */
.hero{left:0;top:108px;width:1200px;height:535px;background:linear-gradient(180deg,#3f4a3e 0%,#2f3b2a 35%,#3d5a2a 65%,#4e6f32 100%)}
.hero-title{left:376px;top:238px;font-size:48px;line-height:56px;color:#fff;letter-spacing:.5px}
.hero-text{left:376px;top:358px;font-size:16px;font-weight:300;color:#fff;line-height:24px}
.hero-cta{left:378px;top:434px;width:147px;height:39px;font-size:16px}

/* why */
.why-photo{left:104px;top:702px;width:407px;height:425px;border-radius:14px;background:linear-gradient(135deg,#0e2a5e,#3d7fc4 45%,#d9e6f1 70%,#f3c766 80%,#1d3f7a)}
.section-title{color:var(--red);font-size:33px}
.why-title{left:585px;top:750px}
.sub{font-size:16px;font-weight:500;color:#111}
.para{font-size:13px;line-height:18px;color:#333}
.explore{left:585px;top:1038px;width:166px;height:38px;font-size:16px}

/* site map */
.map-title{left:0;top:1312px;width:1200px;text-align:center}
.map-desc{left:0;top:1366px;width:1200px;text-align:center;font-size:13px;line-height:18px}
.plan{left:66px;top:1437px;width:535px;height:532px;border-radius:36px;background:var(--maroon)}
.legend{left:120px;top:1458px;display:flex;gap:18px;font-size:10px;font-weight:700;color:#fff}
.legend span{display:flex;align-items:center;gap:5px}
.legend i{width:10px;height:10px;border-radius:50%;display:inline-block}
.plan-area{left:112px;top:1493px;width:438px;height:438px;background:linear-gradient(180deg,#f4d77a,#e8bf57);border-radius:4px}
.shot{left:623px;width:431px;height:164px;border-radius:16px}
.shot1{top:1448px;background:linear-gradient(180deg,#dfe6ee,#9ea9b4 60%,#4f5a60)}
.shot2{top:1621px;background:linear-gradient(180deg,#6e8f5b,#5fb43a 50%,#3e8a24)}
.shot3{top:1794px;background:linear-gradient(180deg,#c7b7b6,#f2c9a5 55%,#3f3a38)}
.avail{left:483px;top:2018px;width:233px;height:39px;font-size:16px}

/* contact */
.person{left:560px;top:2137px;width:640px;height:582px;background:linear-gradient(90deg,rgba(239,239,239,0),#d2d2d2 35%,#b9b9b9 70%,#e2e2e2)}
.help{left:129px;top:2414px;color:var(--red);font-size:18px;font-weight:700}
.field{border:1px solid var(--field);border-radius:16px;background:#fff;font-size:12px;color:#999;padding:10px 14px}
.submit{left:129px;top:2637px;width:120px;height:34px;font-size:16px}

/* footer */
.footer{left:0;top:2719px;width:1200px;height:230px;background:#000;color:#fff}
.foot-brand{left:65px;top:2790px;display:flex;align-items:center;gap:10px}
.foot-brand .brand-dot{width:56px;height:56px}
.foot-brand div:last-child{font-family:"Exo 2",sans-serif;font-weight:800;color:var(--red);font-size:16px;line-height:1.1;width:90px}
.foot-h{font-family:"Exo 2",sans-serif;font-weight:700;font-size:19px;color:#fff;display:flex;align-items:center;gap:8px}
.foot-t{font-size:14px;line-height:20px;color:#ddd}
.small-btn{height:33px;font-size:12px;border-radius:17px}
.phone{right:65px;top:2754px;font-size:31px;color:#fff;font-family:"Exo 2",sans-serif;font-weight:800}
.social{left:977px;top:2868px;display:flex;gap:9px}
.social i{width:33px;height:33px;border-radius:50%;display:block}
.bottom{left:0;top:2949px;width:1200px;height:77px;background:#000;border-top:1px solid #1c1c1c;color:#ccc;font-size:13px}
</style>
</head>
<body>

<header class="abs site-header">
  <div class="abs brand"><div class="brand-dot"></div><div class="brand-name">Pinebrook Commerce Estate</div></div>
  <nav class="abs nav">
    <span class="active">-- HOME --</span><span>WHY PINEBROOK</span><span>SITE MAP &amp; ZONING</span><span>CONTACT</span>
  </nav>
  <a class="abs btn btn-red quick">Quick Inquiry</a>
</header>

<section class="abs hero" role="img" aria-label="Landscaped park with a winding path and trees at dusk">
</section>
<svg class="abs" style="left:0;top:108px" width="1200" height="535" viewBox="0 0 1200 535">
  <path d="M0,270 C200,470 450,540 700,528 C900,518 1080,450 1200,390 L1200,535 L0,535 Z" fill="#f8f8f8"/>
  <path d="M0,225 C180,440 430,522 700,519 L700,528 C450,540 200,470 0,270 Z" fill="#ba0000"/>
  <path d="M640,527 C880,514 1060,440 1200,356 L1200,390 C1080,450 900,518 700,528 Z" fill="#000"/>
</svg>
<h1 class="abs heading hero-title">YOUR COMMERCIAL<br>REAL ESTATE SOLUTION</h1>
<p class="abs hero-text">Lorem Ipsum is simply dummy text of the printing and typesetting industry.<br>Lorem Ipsum has been the industry's standard...</p>
<a class="abs btn btn-outline-white hero-cta">Contact Us</a>

<svg class="abs" style="left:0;top:1090px" width="1200" height="190" viewBox="0 0 1200 190">
  <path d="M0,40 C150,150 350,175 600,120 C820,70 1000,10 1200,40 L1200,0 L0,0 Z" fill="#f8f8f8"/>
</svg>

<div class="abs why-photo" role="img" aria-label="Glass office tower seen from below against a bright sky"></div>
<h2 class="abs heading section-title why-title">WHY PINEBROOK?</h2>
<div class="abs sub" style="left:585px;top:807px">LOCATION ADVANTAGE</div>
<p class="abs para" style="left:585px;top:836px;width:505px">Located approximately 80 kilometers northeast of downtown Edmonton.&nbsp; The two main provincial roadways through the County are Highway 28 and Highway 63.&nbsp; This is the route from the Edmonton region to Fort McMurray, heavily traveled by workers and used to haul equipment and materials to the oil sands.</p>
<div class="abs sub" style="left:585px;top:921px">A NUMBER OF USES</div>
<p class="abs para" style="left:585px;top:950px;width:505px">Industrial lots could serve a number of uses including equipment and pipe storage as well as maintenance shops.&nbsp; Ideal location for a staging area for pipeline companies or storage of materials to be shipped to Fort McMurray.</p>
<a class="abs btn btn-outline-red explore">Explore More</a>

<h2 class="abs heading section-title map-title">SITE MAP &amp; ZONING</h2>
<p class="abs map-desc">The general purpose of this District is to provide opportunities for light industrial and manufacturing uses, with heavier industry<br>permitted in approved locations at the discretion of the Development Authority.</p>

<div class="abs plan"></div>
<div class="abs legend">
  <span><i style="background:#ff2b4f"></i>SOLD</span>
  <span><i style="background:#f2cf6a"></i>PENDING</span>
  <span><i style="background:#b3a35a"></i>AVAILABLE</span>
</div>
<div class="abs plan-area" role="img" aria-label="Interactive lot plan showing numbered parcels 1 to 103 around a loop road"></div>

<div class="abs shot shot1" role="img" aria-label="Row of parked semi trucks"></div>
<div class="abs shot shot2" role="img" aria-label="Aerial view of green land with plot markers"></div>
<div class="abs shot shot3" role="img" aria-label="Industrial processing plant at sunset"></div>

<a class="abs btn btn-red avail">Check Site Availability</a>

<svg class="abs" style="left:0;top:2137px" width="1200" height="582" viewBox="0 0 1200 582">
  <path d="M0,245 C200,200 330,40 600,30 C850,20 1000,40 1200,10 L1200,582 L0,582 Z" fill="#efefef"/>
</svg>
<div class="abs person" role="img" aria-label="Customer support representative wearing a headset, greyscale"></div>

<h3 class="abs help">How May We Help You!</h3>
<div class="abs field" style="left:129px;top:2452px;width:194px;height:34px">Name</div>
<div class="abs field" style="left:340px;top:2452px;width:195px;height:34px">Phone</div>
<div class="abs field" style="left:129px;top:2500px;width:406px;height:34px">Email</div>
<div class="abs field" style="left:129px;top:2549px;width:406px;height:71px">Message</div>
<a class="abs btn btn-red submit">Submit</a>

<footer class="abs footer"></footer>
<div class="abs foot-brand"><div class="brand-dot"></div><div>Pinebrook Commerce Estate</div></div>

<div class="abs foot-h" style="left:296px;top:2763px">
  <svg width="12" height="16" viewBox="0 0 12 16"><path d="M6 0C2.7 0 0 2.6 0 5.8 0 10 6 16 6 16s6-6 6-10.2C12 2.6 9.3 0 6 0zm0 8.2a2.4 2.4 0 110-4.8 2.4 2.4 0 010 4.8z" fill="#ba0000"/></svg>
  PINEBROOK COMMERCE ESTATE</div>
<p class="abs foot-t" style="left:296px;top:2809px">SE Corner Hwy 120<br>and TWP 410</p>
<a class="abs btn small-btn" style="left:296px;top:2868px;width:84px;border:1px solid #fff;color:#fff">Maps</a>

<div class="abs foot-h" style="left:667px;top:2763px">
  <svg width="16" height="13" viewBox="0 0 16 13"><path d="M0 4l8 5 8-5v9H0z M0 2L8 0l8 2-8 5z" fill="#ba0000"/></svg>
  CONTACT US</div>
<p class="abs foot-t" style="left:667px;top:2809px">E-mail address:<br>info@pinebrook-example.com</p>
<a class="abs btn btn-red small-btn" style="left:664px;top:2868px;width:131px">Contact Us</a>

<div class="abs phone">555 013 7268</div>
<div class="abs foot-t" style="right:65px;top:2809px">Available 8:00am - 4:00pm</div>
<div class="abs social"><i style="background:#3b5998"></i><i style="background:#1da1f2"></i><i style="background:#e52d27"></i><i style="background:#0e76a8"></i></div>

<div class="abs bottom">
  <div class="abs" style="left:65px;top:31px">Home &nbsp;&nbsp;|&nbsp;&nbsp; About &nbsp;&nbsp;|&nbsp;&nbsp; Site Availability &nbsp;&nbsp;|&nbsp;&nbsp; Contact</div>
  <div class="abs" style="right:65px;top:31px">Copyright © 2022 Pinebrook Commerce Estate. All Right Reserved</div>
</div>

</body>
</html>
```